Accounting firm for Dentists needs a brochure

We are an accounting firm that specializes in dental practices. We have the information we want attached in a word file. We don't care the number of folds. We would just like it to look professional. Our logo is also attached so you know what our company colors are.

Industry/Entity Type

Accounting

```html
<!DOCTYPE html>
<html lang="en">
<head>
<meta charset="UTF-8">
<title>BrightLedger Dental CPA's Ltd. – Trifold Brochure</title>
<link href="https://fonts.googleapis.com/css2?family=Open+Sans:wght@400;600;700;800&family=Roboto:wght@500;700;900&display=swap" rel="stylesheet">
<style>
  :root{
    --sky:#29a9ea;
    --sky-deep:#1e93d6;
    --sky-pale:#8fd4f6;
    --slate:#4a4c50;
    --slate-dark:#36383b;
    --ink:#3d3f42;
    --paper:#ffffff;
    --backdrop:#d9d9d9;
  }
  *{box-sizing:border-box;margin:0;padding:0}
  html,body{width:1200px;height:900px;overflow:hidden}
  body{background:var(--backdrop);font-family:"Open Sans",Arial,sans-serif;position:relative}
  .brochure{position:absolute;left:60px;top:90px;width:1080px;height:720px;display:flex;box-shadow:0 10px 30px rgba(0,0,0,.25)}
  .panel{position:relative;width:360px;height:720px;overflow:hidden}
  .panel svg.shape{position:absolute;left:0;display:block}

  /* inside-left panel */
  .panel--services{background:var(--paper)}
  .office-photo{position:absolute;left:0;top:0;width:360px;height:225px;background:linear-gradient(135deg,#cfe3f2 0%,#9fc2de 45%,#5f89ad 100%)}
  .services-copy{position:absolute;left:30px;top:238px;width:305px;color:var(--ink)}
  .section-title{font-family:"Roboto",Arial,sans-serif;font-weight:700;color:var(--sky);font-size:15px;line-height:1.15;text-transform:uppercase;margin-bottom:5px}
  .services-copy p{font-size:11px;line-height:1.4;margin-bottom:12px}
  .services-copy strong{font-weight:700;text-transform:uppercase}
  .service-list{list-style:none;margin:-4px 0 10px 14px}
  .service-list li{font-size:11px;font-weight:700;line-height:1.45;position:relative;padding-left:14px}
  .service-list li::before{content:"";position:absolute;left:0;top:6px;width:5px;height:5px;border-radius:50%;background:var(--sky)}
  .closing-note{margin-bottom:0}

  /* middle panel */
  .panel--intro{background:linear-gradient(180deg,var(--sky) 0%,#36b2ee 55%,var(--sky-deep) 100%);color:var(--paper)}
  .intro-copy{position:absolute;left:30px;top:28px;width:300px}
  .intro-copy p{font-size:11px;line-height:1.45;margin-bottom:12px}
  .intro-copy h2{font-family:"Roboto",Arial,sans-serif;font-weight:900;font-size:12.5px;line-height:1.3;color:var(--slate-dark);text-transform:uppercase}
  .growth-chart{top:150px}
  .brand-block{position:absolute;left:0;width:360px;top:462px;text-align:center}
  .brand-name{font-family:"Open Sans",Arial,sans-serif;font-weight:700;line-height:1.05}
  .brand-block .brand-name{color:var(--paper);font-size:32px}
  .brand-block .brand-name span{display:block;font-size:13px;margin-top:4px}
  .contact{margin-top:30px;font-weight:700;font-size:17px;line-height:1.6}

  /* cover panel */
  .panel--cover{background:var(--paper)}
  .cover-brand{position:absolute;left:0;top:40px;width:360px;text-align:center}
  .cover-brand .brand-name{color:var(--sky);font-size:36px}
  .cover-brand .brand-name span{display:block;font-size:14px;margin-top:4px}
  .dentist-photo{position:absolute;left:30px;top:178px;width:300px;height:250px;background:radial-gradient(ellipse at 55% 40%,#f4f7fa 0%,#dfe9f1 55%,#b9d4e8 100%)}
  .cta{position:absolute;left:0;top:470px;width:360px;text-align:center;color:var(--paper);font-family:"Roboto",Arial,sans-serif;font-weight:700}
  .cta-line{font-size:19px;text-transform:uppercase;line-height:1.2}
  .cta-free{font-size:46px;font-weight:900;color:var(--sky);vertical-align:-6px;margin-left:4px}
  .cta-phone{display:inline-block;margin-top:24px;background:var(--sky);color:var(--slate-dark);font-size:28px;font-weight:900;padding:8px 30px;border-radius:30px;letter-spacing:.5px}
</style>
</head>
<body>
<main class="brochure">

  <section class="panel panel--services">
    <div class="office-photo" role="img" aria-label="Photo of accountants' hands working with calculator, papers and laptop on a desk"></div>
    <svg class="shape" style="top:180px" width="360" height="60" viewBox="0 0 360 60" aria-hidden="true">
      <path d="M0 25 C120 60 240 0 360 20 L360 60 L0 60Z" fill="var(--sky)"/>
      <path d="M0 36 C120 70 240 10 360 32 L360 60 L0 60Z" fill="var(--paper)"/>
    </svg>
    <div class="services-copy">
      <h2 class="section-title">Advanced<br>Tax Strategies</h2>
      <p>Tax planning should be more than just finding out what you owe in advance. At BrightLedger Dental CPA's, we pride ourselves in advising in areas of advanced tax mitigation strategies, to reduce your overall tax bill - not just predict it.</p>
      <h2 class="section-title">Our Services</h2>
      <p><strong>At BrightLedger Dental CPA's</strong> we offer a variety of accounting and tax services. Examples of services available include, but are not limited to:</p>
      <ul class="service-list">
        <li>Monthly Bookkeeping</li>
        <li>Bookkeeper Oversight</li>
        <li>Accounting Records Cleanup</li>
        <li>Personal Bookkeeping Services</li>
        <li>Bill Payment and Document Management</li>
        <li>Tax Planning</li>
        <li>Tax Preparation</li>
        <li>Monthly Industry Comparisons</li>
      </ul>
      <p class="closing-note">No matter what your needs, we are committed to delivering accurate, timely and professional accounting services.</p>
    </div>
    <svg class="shape" style="top:662px" width="360" height="58" viewBox="0 0 360 58" aria-hidden="true">
      <path d="M0 30 C120 0 240 40 360 6 L360 58 L0 58Z" fill="var(--sky)"/>
      <path d="M0 42 C120 14 240 52 360 18 L360 58 L0 58Z" fill="var(--slate)"/>
    </svg>
  </section>

  <section class="panel panel--intro">
    <div class="intro-copy">
      <p>At BrightLedger Dental CPA's Ltd., our licensed CPA's have the knowledge to tackle complex tax and accounting issues and the experience to present a clear picture of your financial position.</p>
      <h2>Why not let an independent consultant help you with financial matters so you can focus on growing your practice?</h2>
    </div>
    <svg class="shape growth-chart" width="360" height="290" viewBox="0 0 360 290" aria-hidden="true">
      <g fill="var(--paper)" opacity=".3">
        <rect x="90" y="170" width="28" height="110"/>
        <rect x="126" y="140" width="28" height="140"/>
        <rect x="162" y="110" width="28" height="170"/>
        <rect x="198" y="80" width="28" height="200"/>
        <rect x="234" y="45" width="28" height="235"/>
        <rect x="270" y="15" width="28" height="265"/>
      </g>
      <polyline points="95,250 140,190 165,205 210,120 230,135 262,40" fill="none" stroke="var(--slate-dark)" stroke-width="5" stroke-linejoin="round" stroke-linecap="round"/>
      <polygon points="255,18 276,40 252,48" fill="var(--slate-dark)"/>
    </svg>
    <div class="brand-block">
      <div class="brand-name">BrightLedger<br>Dental<span>CPA's Ltd.</span></div>
      <div class="contact">1-888-555-0142<br>Info@BrightLedgerLtd.com</div>
    </div>
  </section>

  <section class="panel panel--cover">
    <div class="cover-brand">
      <div class="brand-name">BrightLedger Dental<span>CPA's Ltd.</span></div>
    </div>
    <svg class="shape" style="top:150px" width="360" height="50" viewBox="0 0 360 50" aria-hidden="true">
      <path d="M0 20 C120 0 240 0 360 18 L360 50 L0 50Z" fill="var(--slate)"/>
      <path d="M0 30 C120 12 240 12 360 30 L360 50 L0 50Z" fill="var(--sky)"/>
    </svg>
    <svg class="shape" style="top:190px" width="360" height="240" viewBox="0 0 360 240" aria-hidden="true">
      <rect width="360" height="240" fill="var(--sky)"/>
    </svg>
    <div class="dentist-photo" role="img" aria-label="Photo of a smiling dentist in a white coat with stethoscope giving a thumbs up"></div>
    <svg class="shape" style="top:390px" width="360" height="330" viewBox="0 0 360 330" aria-hidden="true">
      <path d="M0 40 C120 0 240 60 360 0 L360 330 L0 330Z" fill="var(--sky)"/>
      <path d="M0 56 C120 18 240 76 360 16 L360 330 L0 330Z" fill="var(--slate)"/>
    </svg>
    <div class="cta">
      <div class="cta-line">Call for a<span class="cta-free">FREE</span></div>
      <div class="cta-line">Quote and Consultation</div>
      <div class="cta-phone">1-888-555-0142</div>
    </div>
  </section>

</main>
</body>
</html>
```